Nordisk Bygnad needs a membership brochure

Nordisk Bygnad is a business association for the Fjordland Joinery Guild ,(our members produce e.g doors, windows, stairs and furniture). We represent 325 businesses, 6500 employees and an annual 1 billion Euro turnover. We need a brochure to attract new members/ customers, but we also need to show existing members what we can offer and what we work for. Our work is political and environmental. We offer legal help, we provide insurance and other member benefits.

Our logo and design manual is 3 years old, and we want the brochure to be founded on our existing colors, which can be found on our website. (www.bygnad.no)

I will provide/write the text for the brochure, as it will be in Norwegian.
To give you some idea, the headlines will be:

What is Nordisk Bygnad?
Legal help
Insurance
HMS
Statistics
Technology
Local branches
Activities:
- Craft Academy
- Timber Fair
- Trade Assembly
- Annual meeting

Target Market(s)

Managers in the Wood Manufacturing industry in Norway

Industry/Entity Type

Political

Font styles to use
Sans Serif
Other font styles liked:
• Arial

Requirements
Must have
• The brochure should have 8 pages. The brochure must be based on our design manual (Profilveileder is uploaded) and our website www.bygnad.no, regarding to colors and fonts.

Use the guidelines "freely".

Nice to have
• It would be nice with some new pictures, but if pictures are needed, i can provide a lot!

```html
<!DOCTYPE html>
<html lang="no">
<head>
<meta charset="utf-8">
<title>Synliggjøring – Nordisk Bygnad</title>
<link href="https://fonts.googleapis.com/css2?family=Arimo:ital,wght@0,400;0,700;1,400&display=swap" rel="stylesheet">
<style>
  :root {
    --paper: #f1dba3;
    --bark: #4a2e1c;
    --leaf: #77953a;
    --ink: #111111;
    --frame: #ffffff;
    --photo-sky: #c9d6df;
    --photo-room: #6f6a64;
  }
  html, body {
    margin: 0;
    padding: 0;
    width: 1200px;
    height: 849px;
    overflow: hidden;
    background: var(--paper);
  }
  .page {
    position: relative;
    width: 1200px;
    height: 849px;
    background: var(--paper);
    font-family: "Arimo", Arial, sans-serif;
    color: var(--ink);
    overflow: hidden;
  }
  .corner {
    position: absolute;
    display: block;
  }
  .corner--top { top: 0; right: 0; }
  .corner--bottom { bottom: 0; left: 0; }
  .hero {
    position: absolute;
    left: 0;
    top: 71px;
    width: 1026px;
    height: 292px;
    background: linear-gradient(180deg, var(--photo-sky) 0%, #b9c6cc 45%, #8a8d85 65%, var(--photo-room) 100%);
  }
  .hero-frame {
    position: absolute;
    left: 0;
    top: 71px;
  }
  .content {
    position: absolute;
    left: 133px;
    width: 955px;
  }
  .title {
    top: 384px;
    margin: 0;
    font-size: 49px;
    font-weight: 700;
    color: var(--leaf);
    letter-spacing: 0.3px;
  }
  .intro {
    top: 449px;
    width: 1000px;
    margin: 0;
    font-size: 17.6px;
    line-height: 1.2;
  }
  .section h2 {
    margin: 0;
    font-size: 17.5px;
    line-height: 21px;
    font-weight: 700;
  }
  .section p {
    margin: 0;
    font-size: 12.3px;
    line-height: 22.5px;
  }
  .section--brand { top: 491px; }
  .section--media { top: 576px; }
  .section--local { top: 649px; }
  .quote {
    top: 754px;
    margin: 0;
    font-size: 12.3px;
    line-height: 22.5px;
    font-style: italic;
  }
</style>
</head>
<body>
<div class="page">
  <svg class="corner corner--top" width="163" height="64" viewBox="0 0 163 64" aria-hidden="true">
    <polygon points="0,0 163,0 163,64" fill="var(--bark)"/>
  </svg>
  <svg class="corner corner--bottom" width="142" height="139" viewBox="0 0 142 139" aria-hidden="true">
    <polygon points="0,0 142,139 0,139" fill="var(--bark)"/>
  </svg>

  <div class="hero" role="img" aria-label="Lys stue med store vindusflater og utsikt mot sjø og kystlandskap"></div>
  <svg class="hero-frame" width="1026" height="292" viewBox="0 0 1026 292" aria-hidden="true">
    <polyline points="204,250 204,2 427,2 469,36 469,290 236,290 204,250" fill="none" stroke="var(--frame)" stroke-width="4"/>
  </svg>

  <h1 class="content title">Synliggjøring</h1>
  <p class="content intro">Nordisk Bygnad skal bidra til å gjøre bransjen mer synlig i samfunnet. Vi jobber både med fagpresse og forbrukerstoff.</p>

  <section class="content section section--brand">
    <h2>Fjordlandsmerket</h2>
    <p>På bygnad.no har vi en medlemsbase hvor forbrukere kan søke opp trevarebedrifter både geografisk og etter produktområde. Som medlem hos oss har du eksklusiv rett til å benytte Nordisk Bygnads logo i ditt markedsmateriell</p>
  </section>

  <section class="content section section--media">
    <h2>Medieovervåking</h2>
    <p>Vi overvåker pressen for hva som skrives om bransjen og våre medlemmer.</p>
  </section>

  <section class="content section section--local">
    <h2>Lokalforeningene</h2>
    <p>I Nordisk Bygnad har vi 11 lokalforeninger. Lokalforeningene er selvstyrte, og møtes med jevne eller ujevne mellomrom. I lokalforeningene er hensikten å skape et lokalt nettverk. De fleste arrangerer bedriftsbesøk og ulike temamøter gjennom året. Dette er en møteplass for å diskutere lokale muligheter og utfordringer. Studieturer og lokale kurs settes også opp jevnlig.</p>
  </section>

  <p class="content quote">"Bare ved å være med på lokalforeningens juleavslutning, skaffet jeg meg oppdrag for 200.000 kroner, på en ellers rolig årstid for oss"&nbsp; Ingrid Haldorsen, Fjellrom Interiør.</p>
</div>
</body>
</html>
```